Business Card Re-Design/Update

We'd like to update out business cards. I've included our current "Style guide" which has the colour scheme of the organisation in it. I've also included the branding files with logos etc in them.

I've also included a copy of one of our existing cards so that you can see how ugly/dated they look. I'd like a fresh modern corporate look.

Target Market(s)

These are for our clients, potential clients, industry contacts - like all business cards

Contact Information for Business Card

Name
Position
Company Address - Level 1, 52 Copperfield Road, Dunmore Qld 4071
Direct Phone
mobile
Email
Website -www.korvelit.com.au
Logo

Colors

Designer to choose colors to be used in the design.

Requirements
Must have
• Main Logo
• Cards will need to be editable to be able to personalize them for each new employee.
Nice to have
• The MapIT, HandIT, KeepIT would be okay to have if they can be sensibly and professionally added to the look without detracting from the main imagery.
• Maybe they could go on the back of the card? will leave this to your creative discretion as to whether/where they fit.
Should not have
• Should not have decorative or script fonts

```html
<!DOCTYPE html>
<html lang="en">
<head>
<meta charset="utf-8">
<title>korvelIT business card</title>
<link href="https://fonts.googleapis.com/css2?family=Open+Sans:wght@400;600;700&display=swap" rel="stylesheet">
<style>
  :root {
    --backdrop: #dcdee0;
    --card-white: #ffffff;
    --brand-red: #d71f26;
    --brand-red-dark: #a3161c;
    --ink: #1c1c1c;
    --ink-soft: #4a4a4a;
    --rule: #9a9a9a;
    --back-black: #1a1a1a;
    --back-black-2: #262626;
  }
  html, body {
    margin: 0;
    padding: 0;
    width: 1200px;
    height: 1200px;
    overflow: hidden;
    background: var(--backdrop);
    font-family: "Open Sans", Arial, sans-serif;
  }
  .canvas {
    position: relative;
    width: 1200px;
    height: 1200px;
  }
  .card {
    position: absolute;
    left: 150px;
    width: 900px;
    height: 514px;
    overflow: hidden;
    box-shadow: 0 6px 18px rgba(0,0,0,0.18);
  }

  /* ---------- front ---------- */
  .card-front {
    top: 62px;
    background: var(--card-white);
  }
  .brand {
    position: absolute;
    left: 70px;
    top: 236px;
    display: flex;
    align-items: center;
    gap: 18px;
  }
  .brand-square {
    width: 46px;
    height: 46px;
    background: var(--brand-red);
  }
  .brand-name {
    font-weight: 700;
    font-size: 58px;
    letter-spacing: -1px;
    color: var(--ink);
    line-height: 1;
  }
  .divider {
    position: absolute;
    left: 520px;
    top: 40px;
    width: 1px;
    height: 200px;
    background: var(--rule);
  }
  .contact {
    position: absolute;
    left: 548px;
    top: 44px;
    color: var(--ink-soft);
    font-size: 15px;
    line-height: 1.55;
  }
  .contact-name {
    color: var(--brand-red);
    font-weight: 700;
    font-size: 24px;
    line-height: 1.2;
    margin: 0 0 4px;
  }
  .contact-role,
  .contact-address { margin: 0; }
  .contact-list {
    list-style: none;
    margin: 8px 0 0;
    padding: 0;
  }
  .contact-list li {
    display: flex;
    align-items: center;
    gap: 10px;
  }
  .contact-icon {
    width: 14px;
    height: 14px;
    flex: none;
  }
  .accent-band {
    position: absolute;
    left: 0;
    top: 372px;
    width: 100%;
    height: 58px;
    background: linear-gradient(90deg, var(--brand-red) 0%, var(--brand-red) 45%, var(--brand-red-dark) 70%, var(--ink) 100%);
  }
  .band-square {
    position: absolute;
    left: 600px;
    top: 382px;
    width: 36px;
    height: 36px;
    background: var(--card-white);
  }
  .edge-strip {
    position: absolute;
    left: 0;
    bottom: 0;
    width: 100%;
    height: 46px;
    background: var(--brand-red);
  }

  /* ---------- back ---------- */
  .card-back {
    top: 624px;
    background: var(--back-black);
  }
  .back-texture {
    position: absolute;
    inset: 0;
    background: linear-gradient(135deg, var(--back-black-2) 0%, var(--back-black) 60%, #141414 100%);
  }
  .tagline {
    position: absolute;
    left: 0;
    right: 0;
    top: 228px;
    text-align: center;
    color: #f2f2f2;
    font-size: 30px;
    font-weight: 400;
    margin: 0;
    letter-spacing: 0.3px;
  }
  .tagline-dot {
    display: inline-block;
    width: 7px;
    height: 7px;
    border-radius: 50%;
    background: var(--brand-red);
    vertical-align: middle;
    margin: 0 12px 0 22px;
    position: relative;
    top: -3px;
  }
  .tagline-dot:first-child { margin-left: 0; }
  .back-square {
    position: absolute;
    right: 110px;
    top: 220px;
    width: 50px;
    height: 50px;
    background: var(--brand-red);
  }
  .back-edge {
    position: absolute;
    left: 0;
    bottom: 0;
    width: 100%;
    height: 8px;
    background: var(--brand-red);
  }
</style>
</head>
<body>
<main class="canvas">

  <section class="card card-front" aria-label="Business card front">
    <div class="brand">
      <span class="brand-square"></span>
      <span class="brand-name">korvelIT</span>
    </div>

    <div class="divider"></div>

    <div class="contact">
      <p class="contact-name">Maren Holloway</p>
      <p class="contact-role">Business Development Manager</p>
      <p class="contact-address">Level 1, 52 Copperfield Road<br>Dunmore Qld 4071</p>
      <ul class="contact-list">
        <li>
          <svg class="contact-icon" viewBox="0 0 16 16"><path fill="#d71f26" d="M3.5 1.5l2.5 3-1.5 1.5c.8 2 2.5 3.7 4.5 4.5L10.5 9l3 2.5-1.5 2.5C7 14 2 9 2 3z"/></svg>
          <span>+61 (07) 3184 5270</span>
        </li>
        <li>
          <svg class="contact-icon" viewBox="0 0 16 16"><rect x="4" y="1" width="8" height="4" fill="#d71f26"/><rect x="1" y="6" width="14" height="6" rx="1" fill="#d71f26"/><rect x="4" y="10" width="8" height="5" fill="#fff" stroke="#d71f26" stroke-width="1.5"/></svg>
          <span>+61 (07) 3184 5270</span>
        </li>
        <li>
          <svg class="contact-icon" viewBox="0 0 16 16"><rect x="1" y="3" width="14" height="10" fill="#d71f26"/><path d="M1.5 3.5L8 9l6.5-5.5" fill="none" stroke="#fff" stroke-width="1.4"/></svg>
          <span>info@korvelit.com.au</span>
        </li>
        <li>
          <svg class="contact-icon" viewBox="0 0 16 16"><circle cx="8" cy="8" r="7" fill="#d71f26"/><path d="M1 8h14M8 1c-3 3-3 11 0 14M8 1c3 3 3 11 0 14" fill="none" stroke="#fff" stroke-width="1"/></svg>
          <span>www.korvelit.com.au</span>
        </li>
      </ul>
    </div>

    <div class="accent-band"></div>
    <div class="band-square"></div>
    <div class="edge-strip"></div>
  </section>

  <section class="card card-back" aria-label="Business card back">
    <div class="back-texture" role="img" aria-label="Faint tonal geometric pattern across the dark background"></div>
    <p class="tagline">
      <span class="tagline-dot"></span>The MapIT<span class="tagline-dot"></span>HandIT<span class="tagline-dot"></span>KeepIT
    </p>
    <div class="back-square"></div>
    <div class="back-edge"></div>
  </section>

</main>
</body>
</html>
```